Business Card Design

I am a self-employed qualified carpenter with the business name Brankwell Joinery. I would like to incorporate the attached logo with a black background with white writing and keep the blue and green that is in my logo if possible.

Industry/Entity Type

Business

Contact Information for Business Card

The attached logo Brankwell Joinery. Marcus Penhallow, Qualified Carpenter, mobile number 0478 562 914, email markpenhallow@quillbox.net, postal address PO Box 617 TARLEE VIC 3291, ABN 47 683 920 514.

```html
<!DOCTYPE html>
<html lang="en">
<head>
<meta charset="utf-8">
<title>Brankwell Joinery – Business Card</title>
<link rel="stylesheet" href="https://fonts.googleapis.com/css2?family=Fira+Sans+Condensed:wght@600;700&family=Arimo:wght@400&display=swap">
<style>
  :root {
    --backdrop: #e4dfd6;
    --band-black: #17181c;
    --stripe-white: #ffffff;
    --wood-light: #eeb04a;
    --wood-mid: #e29c2e;
    --wood-deep: #cf8522;
    --ink: #2a2016;
    --paper-white: #ffffff;
  }
  * { margin: 0; padding: 0; box-sizing: border-box; }
  html, body {
    width: 1200px;
    height: 720px;
    overflow: hidden;
    background: var(--backdrop);
  }
  .canvas {
    position: relative;
    width: 1200px;
    height: 720px;
  }
  .card {
    position: absolute;
    left: 156px;
    top: 86px;
    width: 888px;
    height: 548px;
    overflow: hidden;
  }
  .card__wood {
    position: absolute;
    left: 0;
    top: 196px;
    width: 100%;
    height: 352px;
    background: linear-gradient(100deg, var(--wood-light) 0%, var(--wood-mid) 55%, var(--wood-deep) 100%);
  }
  .card__band {
    position: absolute;
    left: 0;
    top: 0;
    width: 100%;
    height: 180px;
    background: var(--band-black);
  }
  .card__stripe {
    position: absolute;
    left: 0;
    top: 180px;
    width: 100%;
    height: 16px;
    background: var(--stripe-white);
  }
  .business-name {
    position: absolute;
    left: 72px;
    top: 66px;
    font-family: "Fira Sans Condensed", sans-serif;
    font-weight: 700;
    font-size: 46px;
    line-height: 1;
    letter-spacing: 0.5px;
    color: var(--paper-white);
  }
  .brand-seal {
    position: absolute;
    left: 540px;
    top: 59px;
    width: 242px;
    height: 242px;
    border-radius: 50%;
    border: 5px solid var(--stripe-white);
    background: var(--band-black);
    display: flex;
    align-items: center;
    justify-content: center;
    text-align: center;
  }
  .brand-seal__name {
    font-family: "Fira Sans Condensed", sans-serif;
    font-weight: 700;
    font-size: 32px;
    line-height: 1.1;
    color: var(--paper-white);
  }
  .person-name {
    position: absolute;
    left: 61px;
    top: 216px;
    font-family: "Fira Sans Condensed", sans-serif;
    font-weight: 600;
    font-size: 35px;
    line-height: 1;
    color: var(--ink);
  }
  .person-role {
    position: absolute;
    left: 61px;
    top: 260px;
    font-family: "Arimo", sans-serif;
    font-size: 24px;
    line-height: 1;
    color: var(--ink);
  }
  .contact-list {
    position: absolute;
    left: 61px;
    top: 329px;
    list-style: none;
  }
  .contact-list__item {
    display: flex;
    align-items: center;
    height: 40px;
    font-family: "Arimo", sans-serif;
    font-size: 26px;
    line-height: 1;
    color: var(--ink);
  }
  .contact-list__icon {
    width: 26px;
    height: 26px;
    margin-right: 8px;
    flex: none;
  }
  .abn {
    position: absolute;
    left: 66px;
    top: 469px;
    font-family: "Arimo", sans-serif;
    font-size: 26px;
    line-height: 1;
    color: var(--ink);
  }
</style>
</head>
<body>
  <main class="canvas">
    <section class="card" aria-label="Business card for Brankwell Joinery">
      <div class="card__wood" role="img" aria-label="Warm honey-toned timber grain texture"></div>
      <div class="card__band"></div>
      <div class="card__stripe"></div>

      <h1 class="business-name">Brankwell Joinery</h1>

      <div class="brand-seal">
        <span class="brand-seal__name">Brankwell<br>Joinery</span>
      </div>

      <h2 class="person-name">Marcus Penhallow</h2>
      <p class="person-role">Qualified Carpenter</p>

      <ul class="contact-list">
        <li class="contact-list__item">
          <svg class="contact-list__icon" viewBox="0 0 26 26" aria-hidden="true">
            <circle cx="13" cy="13" r="11.5" fill="none" stroke="#2a2016" stroke-width="1.6"/>
            <path d="M9 7.5c-1 .6-1.6 1.6-1.4 3 .5 3.4 4.4 7.5 7.8 8.1 1.3.2 2.3-.3 2.9-1.3l-2.2-1.8-1.4 1c-1.6-.7-3.2-2.4-3.8-4l1-1.4z" fill="#2a2016"/>
          </svg>
          0478 562 914
        </li>
        <li class="contact-list__item">
          <svg class="contact-list__icon" viewBox="0 0 26 26" aria-hidden="true">
            <path d="M2.5 10.5 13 3.5l10.5 7V22h-21z" fill="none" stroke="#2a2016" stroke-width="1.8" stroke-linejoin="round"/>
            <path d="M2.5 10.5 13 16.5l10.5-6M2.5 22l8-7M23.5 22l-8-7" fill="none" stroke="#2a2016" stroke-width="1.8" stroke-linejoin="round"/>
          </svg>
          markpenhallow@quillbox.net
        </li>
        <li class="contact-list__item">
          <svg class="contact-list__icon" viewBox="0 0 26 26" aria-hidden="true">
            <path d="M13 2a7 7 0 0 0-7 7c0 5 7 15 7 15s7-10 7-15a7 7 0 0 0-7-7z" fill="#2a2016"/>
            <circle cx="13" cy="9" r="2.6" fill="#e6a43a"/>
          </svg>
          PO Box 617 TARLEE VIC 3291
        </li>
      </ul>

      <p class="abn">ABN 47 683 920 514</p>
    </section>
  </main>
</body>
</html>
```